Drifting Earwaves - listen to podcasts from around the world

http://randompodcasts.com/Drifting Earwaves lets you listen to randomly selected podcasts from around the world. You can filter the podcasts by language. The power of randomness allows you to escape filter bubbles and echo chambers and discover issues and perspectives that you never knew existed. The current website offers basic functionality and is only a demo. Don't assume that anything in the current "design" should stay in place. The goal of the design should be to make it as easy as possible to understand what the app offers, to listen to new podcasts, and to skip to the next podcast. The service will be offered both as mobile apps and directly on the website. We expect that most users will be on mobile devices which is why we are focusing on the mobile/web app design.In addition to the current functionality, the app should also offer search (allowing the user to listen to podcasts that match given keywords), allow the user to easily subscribe to the current podcast and show the profile picture of the current podcast.

Target Market(s)

People interested in podcasts, all around the world

Colors

Designer to choose colors to be used in the design.

Requirements
Must have
• The main challenge is how to communicate the concept of the app to the user. Podcasts are randomly selected and the user just skips to the next one when he/she wants to. The ability to filter podcasts by language is important but no other filters are needed. The point is to use the power of random selection to explore new surprising content.
Nice to have
• The app/website is targeting a global audience. The less reliant the design is on written language, the better.

```html
<!DOCTYPE html>
<html lang="en">
<head>
<meta charset="utf-8">
<title>Drifting Earwaves</title>
<link rel="stylesheet" href="https://fonts.googleapis.com/css2?family=Mulish:wght@400;600;700;800&family=Noto+Sans+Oriya:wght@400;600&display=swap">
<style>
  :root{
    --bg-top:#d35cc4;
    --bg-bottom:#f0668a;
    --white:#ffffff;
    --header:#ffffff;
    --title-grey:#d9d9d9;
    --ink:#222222;
    --muted:#8a8a8a;
    --card-purple:#2a0f5e;
    --card-photo-a:#9a7f86;
    --card-photo-b:#6e5a66;
    --card-photo-c:#8a6e7a;
    --side-card-a:#b99aa7;
    --side-card-b:#f36c86;
    --episode-bg:#f5cfe1;
    --nav-bg:#f3f3f3;
    --nav-line:#e2e2e2;
    --nav-text:#8c8c8c;
    --track:rgba(255,255,255,.45);
  }
  html,body{margin:0;padding:0;width:1200px;height:2598px;overflow:hidden;background:#ffffff}
  .screen{
    position:absolute;left:0;top:0;width:375px;height:812px;
    transform:scale(3.2);transform-origin:0 0;overflow:hidden;
    font-family:"Mulish",sans-serif;
    background:linear-gradient(180deg,var(--bg-top) 0%,#df60ad 45%,var(--bg-bottom) 100%);
  }
  .abs{position:absolute}
  .header{left:0;top:0;width:375px;height:93px;background:var(--header)}
  .status-time{left:30px;top:14px;font-size:15px;font-weight:700;color:var(--ink);letter-spacing:-.2px}
  .status-icons{right:18px;top:16px}
  .menu-icon{left:21px;top:55px}
  .app-title{left:0;width:375px;top:50px;text-align:center;font-size:19px;color:var(--title-grey);letter-spacing:1.2px;font-weight:400}
  .tagline{left:25px;top:99px;width:335px;font-size:13px;line-height:24px;color:var(--white);letter-spacing:.35px;font-weight:600}
  .side-card{top:205px;height:246px;border-radius:10px;background:linear-gradient(180deg,var(--side-card-a) 0%,#c78496 60%,var(--side-card-b) 100%)}
  .side-left{left:-40px;width:70px}
  .side-right{left:345px;width:70px}
  .podcast-card{left:48px;top:159px;width:280px;height:292px;border-radius:10px;overflow:hidden;box-shadow:0 6px 18px rgba(60,0,60,.25)}
  .podcast-photo{position:absolute;inset:0;background:linear-gradient(160deg,var(--card-photo-a) 0%,var(--card-photo-c) 40%,var(--card-photo-b) 65%,#4a2a5e 100%)}
  .podcast-shade{position:absolute;inset:0;background:linear-gradient(180deg,rgba(42,15,94,0) 45%,rgba(42,15,94,.85) 80%,var(--card-purple) 100%)}
  .podcast-info{position:absolute;left:0;right:0;top:222px;text-align:center}
  .podcast-name{font-size:13px;font-weight:700;color:var(--white);letter-spacing:.6px}
  .podcast-meta{font-size:11px;color:#c9a9d6;margin-top:6px;letter-spacing:.3px}
  .podcast-host{font-size:11px;color:#c9a9d6;margin-top:6px;letter-spacing:.3px}
  .track{left:20px;top:522px;width:335px;height:2px;background:var(--track);border-radius:1px}
  .track-fill{left:20px;top:521px;width:76px;height:3px;background:var(--white);border-radius:2px}
  .knob{left:81px;top:508px;width:30px;height:30px;border-radius:50%;background:var(--white);box-shadow:0 2px 6px rgba(0,0,0,.15)}
  .time{top:540px;font-size:9px;font-weight:800;color:var(--white)}
  .time-start{left:20px}
  .time-end{left:334px}
  .control{top:585px}
  .like-count{left:21px;top:602px;width:20px;text-align:center;font-size:8px;font-weight:800;color:var(--white)}
  .episode-card{left:21px;top:636px;width:333px;height:140px;border-radius:10px;background:var(--episode-bg)}
  .episode-icon{left:24px;top:27px}
  .episode-label{left:53px;top:24px;font-size:13px;font-weight:800;color:var(--ink);letter-spacing:1px}
  .episode-title{left:139px;top:26px;font-family:"Noto Sans Oriya","Mulish",sans-serif;font-size:13px;line-height:26px;color:var(--ink);width:180px}
  .episode-sub{left:139px;top:79px;font-size:12px;color:var(--ink);opacity:.7}
  .bottom-nav{left:0;top:727px;width:375px;height:85px;background:var(--nav-bg);display:flex}
  .nav-item{flex:1;position:relative;text-align:center;border-right:1px solid var(--nav-line)}
  .nav-item:last-child{border-right:none}
  .nav-item svg{position:absolute;left:50%;top:10px;transform:translateX(-50%)}
  .nav-label{position:absolute;left:0;right:0;top:38px;font-size:9px;color:var(--nav-text)}
  .home-indicator{left:120px;top:798px;width:134px;height:5px;border-radius:3px;background:#222}
</style>
</head>
<body>
<main class="screen">
  <header class="abs header">
    <div class="abs status-time">9:41</div>
    <svg class="abs status-icons" width="60" height="12" viewBox="0 0 60 12" aria-hidden="true">
      <rect x="0" y="8" width="3" height="4" rx="1" fill="#222"/>
      <rect x="5" y="6" width="3" height="6" rx="1" fill="#222"/>
      <rect x="10" y="3" width="3" height="9" rx="1" fill="#222"/>
      <rect x="15" y="0" width="3" height="12" rx="1" fill="#222"/>
      <path d="M24 4 a10 10 0 0 1 14 0 M27 7 a6 6 0 0 1 8 0" stroke="#222" stroke-width="1.6" fill="none"/>
      <circle cx="31" cy="10.5" r="1.4" fill="#222"/>
      <rect x="42" y="1" width="16" height="10" rx="2.5" fill="none" stroke="#999"/>
      <rect x="44" y="3" width="12" height="6" rx="1" fill="#222"/>
    </svg>
    <svg class="abs menu-icon" width="18" height="12" viewBox="0 0 18 12" aria-label="Menu">
      <rect x="0" y="0" width="16" height="1.6" fill="#555"/>
      <rect x="2" y="3.5" width="14" height="1.6" fill="#555"/>
      <rect x="0" y="7" width="16" height="1.6" fill="#555"/>
      <rect x="2" y="10.4" width="14" height="1.6" fill="#555"/>
    </svg>
    <h1 class="abs app-title" style="margin:0">Drifting Earwaves</h1>
  </header>

  <p class="abs tagline" style="margin:0">Travel outside of your echo chamber and filter bubble, listen to podcasts from around the world</p>

  <div class="abs side-card side-left" role="img" aria-label="Previous podcast cover photo"></div>
  <div class="abs side-card side-right" role="img" aria-label="Next podcast cover photo"></div>

  <article class="abs podcast-card">
    <div class="podcast-photo" role="img" aria-label="Podcast cover photo: street musicians playing to a crowd"></div>
    <div class="podcast-shade"></div>
    <div class="podcast-info">
      <div class="podcast-name">Our Silver Lantern</div>
      <div class="podcast-meta">English (feed, detected)</div>
      <div class="podcast-host">Humming ( Marisol )</div>
    </div>
  </article>

  <div class="abs track"></div>
  <div class="abs track-fill"></div>
  <div class="abs knob"></div>
  <div class="abs time time-start">0.12</div>
  <div class="abs time time-end">2.12</div>

  <svg class="abs control" style="left:25px" width="13" height="12" viewBox="0 0 24 22" aria-label="Like">
    <path d="M12 20 C4 14 1 10 1 6.5 A5.5 5.5 0 0 1 12 4 A5.5 5.5 0 0 1 23 6.5 C23 10 20 14 12 20Z" fill="none" stroke="#fff" stroke-width="2.2"/>
  </svg>
  <div class="abs like-count">1.2k</div>
  <svg class="abs control" style="left:91px" width="12" height="12" viewBox="0 0 12 12" aria-label="Previous">
    <path d="M1.5 1 V11" stroke="#fff" stroke-width="1.4"/>
    <path d="M10.5 1.5 L3.5 6 L10.5 10.5Z" fill="none" stroke="#fff" stroke-width="1.3" stroke-linejoin="round"/>
  </svg>
  <svg class="abs control" style="left:179px" width="12" height="12" viewBox="0 0 12 12" aria-label="Play">
    <path d="M2 1 L10.5 6 L2 11Z" fill="none" stroke="#fff" stroke-width="1.3" stroke-linejoin="round"/>
  </svg>
  <svg class="abs control" style="left:268px" width="12" height="12" viewBox="0 0 12 12" aria-label="Next">
    <path d="M1.5 1.5 L8.5 6 L1.5 10.5Z" fill="none" stroke="#fff" stroke-width="1.3" stroke-linejoin="round"/>
    <path d="M10.5 1 V11" stroke="#fff" stroke-width="1.4"/>
  </svg>
  <svg class="abs control" style="left:341px" width="13" height="13" viewBox="0 0 13 13" aria-label="Download">
    <path d="M6.5 1 V8.5 M3.5 5.5 L6.5 8.5 L9.5 5.5" fill="none" stroke="#fff" stroke-width="1.3"/>
    <path d="M1 9 V12 H12 V9" fill="none" stroke="#fff" stroke-width="1.3"/>
  </svg>

  <section class="abs episode-card">
    <svg class="abs episode-icon" width="12" height="12" viewBox="0 0 12 12" aria-hidden="true">
      <rect x="0.5" y="0.5" width="11" height="11" fill="none" stroke="#222"/>
      <rect x="3" y="0.5" width="6" height="11" fill="#222"/>
      <rect x="0.5" y="2.5" width="2" height="1.5" fill="#222"/>
      <rect x="0.5" y="5.5" width="2" height="1.5" fill="#222"/>
      <rect x="0.5" y="8.5" width="2" height="1.5" fill="#222"/>
      <rect x="9.5" y="2.5" width="2" height="1.5" fill="#222"/>
      <rect x="9.5" y="5.5" width="2" height="1.5" fill="#222"/>
      <rect x="9.5" y="8.5" width="2" height="1.5" fill="#222"/>
    </svg>
    <div class="abs episode-label">Episode</div>
    <div class="abs episode-title">856 ସେମାନଙ୍କ ଜୋତା ପିନ୍ଧି ଚାଲିବା</div>
    <div class="abs episode-sub">Walking in their shoes</div>
  </section>

  <nav class="abs bottom-nav">
    <div class="nav-item">
      <svg width="20" height="20" viewBox="0 0 20 20" aria-hidden="true">
        <rect x="1" y="1" width="11" height="11" rx="1" fill="none" stroke="#555" stroke-width="1.2"/>
        <path d="M4 4 H9 M6.5 3 V4 M8 4 C7 7 5.5 9 3.5 10 M5 6 C6 8 8 9.5 9.5 10" fill="none" stroke="#555" stroke-width="1"/>
        <rect x="8" y="8" width="11" height="11" rx="1" fill="#fff" stroke="#555" stroke-width="1.2"/>
        <path d="M11 17 L13.5 10.5 L16 17 M12 15 H15" fill="none" stroke="#555" stroke-width="1"/>
      </svg>
      <span class="nav-label">Selected Language</span>
    </div>
    <div class="nav-item">
      <svg width="20" height="20" viewBox="0 0 20 20" aria-hidden="true">
        <rect x="1" y="1" width="11" height="11" rx="1" fill="none" stroke="#555" stroke-width="1.2"/>
        <path d="M4 4 H9 M6.5 3 V4 M8 4 C7 7 5.5 9 3.5 10 M5 6 C6 8 8 9.5 9.5 10" fill="none" stroke="#555" stroke-width="1"/>
        <rect x="8" y="8" width="11" height="11" rx="1" fill="#fff" stroke="#555" stroke-width="1.2"/>
        <path d="M11 17 L13.5 10.5 L16 17 M12 15 H15" fill="none" stroke="#555" stroke-width="1"/>
      </svg>
      <span class="nav-label">Language</span>
    </div>
    <div class="nav-item">
      <svg width="20" height="20" viewBox="0 0 20 20" aria-hidden="true">
        <rect x="1" y="1" width="11" height="11" rx="1" fill="none" stroke="#555" stroke-width="1.2"/>
        <path d="M4 4 H9 M6.5 3 V4 M8 4 C7 7 5.5 9 3.5 10 M5 6 C6 8 8 9.5 9.5 10" fill="none" stroke="#555" stroke-width="1"/>
        <rect x="8" y="8" width="11" height="11" rx="1" fill="#fff" stroke="#555" stroke-width="1.2"/>
        <path d="M11 17 L13.5 10.5 L16 17 M12 15 H15" fill="none" stroke="#555" stroke-width="1"/>
      </svg>
      <span class="nav-label">Default Language</span>
    </div>
  </nav>
  <div class="abs home-indicator"></div>
</main>
</body>
</html>
```